Business card, folder, and other items for LMV
Lakemoor Vale Oncology, PLLC business cards and material
Please show us folder designs that will house these documents as well.
Thanks for all the great designs.
After seeing double sided designs above, we would like to utilize this design feature. Please submit double sided designs. Thank you.
Please show designs of folder and stationery as well. Current designs look very nice. Thanks for the submissions.

```html
<!DOCTYPE html>
<html lang="en">
<head>
<meta charset="utf-8">
<title>LMV business card</title>
<link rel="stylesheet" href="https://fonts.googleapis.com/css2?family=Arimo:wght@400;700&display=swap">
<style>
  :root {
    --page-bg: #ecebe8;
    --card-white: #ffffff;
    --blue-deep: #1f3f96;
    --blue-mid: #2c5cb6;
    --blue-light: #4c82d6;
    --swoosh-grey: #c9ccd2;
    --logo-blue: #2a5bb0;
    --text-white: #ffffff;
  }
  * { margin: 0; padding: 0; box-sizing: border-box; }
  html, body {
    width: 1200px;
    height: 778px;
    overflow: hidden;
    background: var(--page-bg);
    font-family: "Arimo", Arial, sans-serif;
  }
  .business-card {
    position: absolute;
    left: 163px;
    top: 157px;
    width: 874px;
    height: 463px;
    border-radius: 26px;
    overflow: hidden;
    background: var(--card-white);
  }
  .card-background {
    position: absolute;
    inset: 0;
    width: 100%;
    height: 100%;
  }
  .brand-mark {
    position: absolute;
    left: 22px;
    top: 150px;
    display: flex;
    align-items: center;
    gap: 14px;
  }
  .brand-dot {
    width: 62px;
    height: 62px;
    border-radius: 50%;
    background: var(--logo-blue);
  }
  .brand-name {
    font-size: 112px;
    font-weight: 700;
    line-height: 1;
    color: var(--logo-blue);
    letter-spacing: 1px;
  }
  .contact-block {
    position: absolute;
    left: 533px;
    top: 76px;
    color: var(--text-white);
  }
  .person-name {
    font-size: 27px;
    font-weight: 400;
    line-height: 1.2;
  }
  .person-title {
    font-size: 21px;
    font-weight: 700;
    margin-top: 4px;
  }
  .postal-address {
    font-style: normal;
    font-size: 20px;
    line-height: 34px;
    margin-top: 44px;
  }
  .contact-lines {
    list-style: none;
    margin-top: 30px;
    font-size: 20px;
    line-height: 34px;
  }
  .contact-lines li {
    display: flex;
    align-items: center;
    gap: 10px;
  }
  .contact-icon {
    width: 17px;
    height: 17px;
    flex: none;
  }
</style>
</head>
<body>
  <div class="business-card">
    <svg class="card-background" viewBox="0 0 874 463" preserveAspectRatio="none" aria-hidden="true">
      <defs>
        <linearGradient id="blueSweep" x1="0" y1="0" x2="1" y2="1">
          <stop offset="0" stop-color="var(--blue-light)"/>
          <stop offset="0.45" stop-color="var(--blue-mid)"/>
          <stop offset="1" stop-color="var(--blue-deep)"/>
        </linearGradient>
      </defs>
      <path d="M360 0 C470 80 500 260 240 463 L874 463 L874 0 Z" fill="var(--swoosh-grey)"/>
      <path d="M390 0 C500 110 500 300 200 463 L874 463 L874 0 Z" fill="url(#blueSweep)"/>
    </svg>

    <div class="brand-mark">
      <span class="brand-dot"></span>
      <span class="brand-name">LMV</span>
    </div>

    <div class="contact-block">
      <p class="person-name">Mara Kherwin, M.D., DABR</p>
      <p class="person-title">President</p>
      <address class="postal-address">
        P.O. Box 2480<br>
        Lakemoor, KY 41190-2480
      </address>
      <ul class="contact-lines">
        <li>
          <svg class="contact-icon" viewBox="0 0 16 16" aria-hidden="true"><path d="M3.5 1.5l2.5 2.5-1.5 2a8 8 0 0 0 5.5 5.5l2-1.5 2.5 2.5-2 2C6 15 1 10 1.5 3.5z" fill="#fff"/></svg>
          1-606-555-0182
        </li>
        <li>
          <svg class="contact-icon" viewBox="0 0 16 16" aria-hidden="true"><rect x="1" y="3" width="14" height="10" fill="none" stroke="#fff" stroke-width="1.6"/><path d="M1 3l7 6 7-6" fill="none" stroke="#fff" stroke-width="1.6"/></svg>
          mkherwin@lakemoorvaleonc.com
        </li>
        <li>
          <svg class="contact-icon" viewBox="0 0 16 16" aria-hidden="true"><circle cx="8" cy="8" r="7" fill="#fff"/><path d="M1 8h14M8 1c-3 3-3 11 0 14M8 1c3 3 3 11 0 14" fill="none" stroke="#2c5cb6" stroke-width="1.2"/></svg>
          www.lakemoorvaleonc.com
        </li>
      </ul>
    </div>
  </div>
</body>
</html>
```